An KADORI MIRETSU certified teacher needs a Business Card Design.

I need a business card to introduce and promote myself as an KADORI MIRETSU certified teacher and florist for fresh floral decoration services of venues ranging from executive rooms to large business and social events. I would prefer sober card with coloured avatar or vector image of a simple KADORI MIRETSU arrangement that has clear floral impression on the business card with my face book, and website address and other contact details like skype, cell and landlines, etc.
I have Teachers Fourth Grade Diploma, and Teaching Membership of Miretsu Mentors Guild (MMG), Japan.

Target Market(s)

Hospitality industry (Hotels, Cafes, Residency), Business organisations (executive rooms, meeting areas, conferences), Individuals & families (parties, social events), Hospitals and Clinics, etc.

Industry/Entity Type

Teacher

Contact Information for Business Card

Nazneen Bilqees
Certified Teacher, Miretsu Academy of Kadori
Cell: +92 317 604 5192
email: petalworx.pk@bloomvia.example
Friendloop: http://www.facebook-sample.example/petalworx.pk
Website: www.petalworx.example

Requirements
Nice to have
• Avatar or vector of a classic/basic KADORI MIRETSU arrangement with vivid colour flowers
Should not have
• images of living things like women, etc.

```html
<!DOCTYPE html>
<html lang="en">
<head>
<meta charset="utf-8">
<title>Nazneen Bilqees – Business Card</title>
<link rel="stylesheet" href="https://fonts.googleapis.com/css2?family=Alegreya:wght@700&family=Questrial&display=swap">
<style>
  :root {
    --backdrop-light: #fdfdf2;
    --backdrop-warm: #f3f6d6;
    --card-white: #ffffff;
    --leaf-green: #c6e2a2;
    --leaf-pale: #e8f3da;
    --ink-dark: #47433b;
    --ink-soft: #55514b;
    --bloom-orange: #e8752a;
    --bloom-red: #c8321e;
    --stem-green: #7fbf3e;
  }
  * { margin: 0; padding: 0; box-sizing: border-box; }
  html, body { width: 1200px; height: 1000px; overflow: hidden; }
  body {
    background: radial-gradient(ellipse at 20% 15%, var(--backdrop-light) 0%, var(--backdrop-warm) 100%);
    position: relative;
  }
  .business-card {
    position: absolute;
    left: 143px; top: 216px;
    width: 894px; height: 503px;
    background: var(--card-white);
    overflow: hidden;
  }
  .card-wave { position: absolute; inset: 0; }
  .arrangement-art {
    position: absolute;
    left: 36px; top: 26px;
    width: 260px; height: 212px;
    border-radius: 46% 54% 48% 52%;
    background: radial-gradient(circle at 30% 68%, var(--bloom-orange) 0%, var(--bloom-red) 20%, rgba(127,191,62,0.5) 46%, rgba(232,243,218,0) 72%);
  }
  .holder-name {
    position: absolute;
    left: 228px; top: 76px; width: 600px;
    text-align: center;
    font-family: "Alegreya", Georgia, serif;
    font-weight: 700;
    font-size: 58px;
    letter-spacing: 2px;
    color: var(--ink-dark);
  }
  .holder-role {
    position: absolute;
    left: 271px; top: 166px; width: 500px;
    text-align: center;
    font-family: "Questrial", Arial, sans-serif;
    font-size: 36px;
    line-height: 42px;
    color: var(--ink-soft);
  }
  .contact-list {
    position: absolute;
    left: 50px; top: 339px;
    list-style: none;
    font-family: "Questrial", Arial, sans-serif;
    font-size: 27px;
    line-height: 34px;
    color: var(--ink-soft);
  }
</style>
</head>
<body>
  <section class="business-card">
    <svg class="card-wave" width="894" height="503" viewBox="0 0 894 503" aria-hidden="true">
      <defs>
        <linearGradient id="leafWash" x1="0" y1="1" x2="1" y2="0.3">
          <stop offset="0" stop-color="#c6e2a2"/>
          <stop offset="0.35" stop-color="#e3f0d2"/>
          <stop offset="0.75" stop-color="#ffffff"/>
        </linearGradient>
      </defs>
      <path fill="url(#leafWash)" d="M0 0 L187 0 C250 25 305 60 300 110 C292 170 215 230 220 300 C224 345 280 360 360 364 C520 372 640 380 760 503 L0 503 Z"/>
    </svg>
    <div class="arrangement-art" role="img" aria-label="Vector Kadori Miretsu arrangement: orange and red bloom with green leaf blades, curling brown branches and small purple blossoms"></div>
    <h1 class="holder-name">Nazneen Bilqees</h1>
    <p class="holder-role">Kadori Miretsu<br>Qualified florist</p>
    <ul class="contact-list">
      <li>cell: +92 317 604 5192</li>
      <li>website: www.petalworx.example</li>
      <li>email: petalworx.pk@bloomvia.example</li>
      <li>friendloop: http://www.friendloop.example/petalworx.pk</li>
    </ul>
  </section>
</body>
</html>
```